Heritage Hollow Business Cards

Require a business card design. <br/><br/>Needs to include logo (either round or long version) plus these details:<br/>Maya Torvel<br/>Heritage Hollow<br/>maya@quonbrook.com.au<br/>02 6481 7390<br/>PO Box Glenwarra NSW 2913<br/>www.heritagehollow.com.au<br/><br/>I need in an editable format so that I can create for multiple staff members. <br/><br/>

Target Market(s)

We are an online store selling renovation products to home owners are builders. Looking for a classic classy design.

Industry/Entity Type

Home And Garden

Contact Information for Business Card

Maya Torvel
Heritage Hollow
maya@quonbrook.com.au
02 6481 7390
PO Box Glenwarra NSW 2913
www.heritagehollow.com.au

Colors

Designer to choose colors to be used in the design.

Requirements
Must have
• Must include Logo.

```html
<!DOCTYPE html>
<html lang="en">
<head>
<meta charset="utf-8">
<title>Heritage Hollow – Business Card</title>
<link href="https://fonts.googleapis.com/css2?family=Open+Sans:wght@400;700&display=swap" rel="stylesheet">
<style>
  :root {
    --stage: #d9dada;
    --card-white: #ffffff;
    --card-grey: #8a8a8a;
    --icon-tile: #c4c4c4;
    --logo-grey: #8c8c8c;
    --text-light: #ffffff;
  }
  html, body {
    margin: 0;
    padding: 0;
    width: 1200px;
    height: 915px;
    overflow: hidden;
    background: var(--stage);
    font-family: "Open Sans", sans-serif;
  }
  .business-card {
    position: absolute;
    left: 75px;
    top: 158px;
    width: 1050px;
    height: 598px;
    overflow: hidden;
    background: var(--card-grey);
  }
  .card-shapes {
    position: absolute;
    inset: 0;
    width: 1050px;
    height: 598px;
  }
  .brand-mark {
    position: absolute;
    left: 66px;
    top: 154px;
    width: 322px;
    height: 322px;
    box-sizing: border-box;
    border: 2px solid var(--logo-grey);
    border-radius: 50%;
    display: flex;
    align-items: center;
    justify-content: center;
  }
  .brand-name {
    margin: 0;
    color: var(--logo-grey);
    font-size: 40px;
    font-weight: 400;
    line-height: 1.1;
    text-align: center;
  }
  .contact-block {
    position: absolute;
    right: 85px;
    top: 176px;
    color: var(--text-light);
    text-align: right;
  }
  .person-name {
    margin: 0 0 50px;
    font-size: 30px;
    font-weight: 400;
    line-height: 44px;
  }
  .person-name .surname { font-weight: 700; }
  .contact-list {
    list-style: none;
    margin: 0;
    padding: 0;
  }
  .contact-item {
    position: relative;
    font-size: 26px;
    line-height: 40px;
  }
  .contact-icon {
    position: absolute;
    right: -42px;
    top: 7px;
    width: 26px;
    height: 26px;
    border-radius: 4px;
    background: var(--icon-tile);
  }
  .contact-icon svg { display: block; width: 26px; height: 26px; }
</style>
</head>
<body>
  <div class="business-card">
    <svg class="card-shapes" viewBox="0 0 1050 598" role="img" aria-label="Grey panel with a faint repeating lattice pattern, separated from the white logo side by curved bands">
      <rect width="1050" height="598" fill="var(--card-grey)"/>
      <path d="M0 0 L362 0 Q593 299 392 598 L0 598 Z" fill="var(--card-white)"/>
      <path d="M0 0 L354 0 Q558 299 350 598 L0 598 Z" fill="var(--card-grey)"/>
      <path d="M0 0 L332 0 Q547 299 302 598 L0 598 Z" fill="var(--card-white)"/>
    </svg>

    <div class="brand-mark">
      <p class="brand-name">Heritage<br>Hollow</p>
    </div>

    <div class="contact-block">
      <h1 class="person-name">Maya <span class="surname">TORVEL</span></h1>
      <ul class="contact-list">
        <li class="contact-item">02 6481 7390
          <span class="contact-icon"><svg viewBox="0 0 26 26"><path d="M8 6 l3 0 l1.5 4 l-2 1.5 q1.5 3 4 4 l1.5-2 l4 1.5 l0 3 q-1 1.5-3 1.5 q-10-1-11-11 q0-2 2-2.5z" fill="var(--card-grey)"/></svg></span>
        </li>
        <li class="contact-item">PO Box Glenwarra NSW 2913
          <span class="contact-icon"><svg viewBox="0 0 26 26"><path d="M13 5 a5 5 0 0 1 5 5 q0 4-5 11 q-5-7-5-11 a5 5 0 0 1 5-5z" fill="var(--card-grey)"/><circle cx="13" cy="10" r="2" fill="var(--icon-tile)"/></svg></span>
        </li>
        <li class="contact-item">maya@quonbrook.com.au
          <span class="contact-icon"><svg viewBox="0 0 26 26"><rect x="6" y="8" width="14" height="10" fill="var(--card-grey)"/><path d="M6 8 l7 5 l7-5" fill="none" stroke="var(--icon-tile)" stroke-width="1.2"/></svg></span>
        </li>
        <li class="contact-item">www.heritagehollow.com.au</li>
      </ul>
    </div>
  </div>
</body>
</html>
```